Professional Business Card for a Chief Operating Officer

An exciting business card that's professional for a c-suite position.
Parent company on the front with information. (CLEAR HARBOR)
3 Brands on the back in a dark blue background.

No icons for phone, email or address.
The card can be vertically laid out or horizontally, whichever fits best.

I'd like to see designs in both formats.
Cards can be designed with a "linen" look or embossed with tone-on-tone as an option.

Target Market(s)

Industry professionals, customers and vendors

Industry/Entity Type

Car Wash

Contact Information for Business Card

Name, title, address, phone, email and logo

Colors
0054AA
0677BA
7BADD7
CADEEF
E8F1F8

Requirements
Must have
• A professional conservative look
Nice to have
• Parent Brand on front, Brand logos on back
Should not have
• Icons

```html
<!DOCTYPE html>
<html lang="en">
<head>
<meta charset="utf-8">
<title>Clear Harbor Carwash – Business Card</title>
<link rel="stylesheet" href="https://fonts.googleapis.com/css2?family=Montserrat:wght@400;500;700&display=swap">
<style>
  :root {
    --bg: #979797;
    --card-front: #ffffff;
    --card-back: #152042;
    --brand-blue: #4689c9;
    --brand-deep: #0054aa;
    --ink: #3a3a3a;
    --light-blue: #7badd7;
    --white: #ffffff;
  }
  * { margin: 0; padding: 0; box-sizing: border-box; }
  html, body { width: 1200px; height: 1059px; overflow: hidden; }
  body {
    background: var(--bg);
    font-family: "Montserrat", sans-serif;
    position: relative;
  }
  .card {
    position: absolute;
    border-radius: 20px;
    overflow: hidden;
  }
  .card-front {
    left: 256px; top: 89px; width: 688px; height: 390px;
    background: var(--card-front);
  }
  .card-back {
    left: 253px; top: 569px; width: 694px; height: 394px;
    background: var(--card-back);
  }
  .parent-mark {
    position: absolute;
    left: 50px; top: 160px;
    display: flex; align-items: center; gap: 12px;
  }
  .parent-mark .dot {
    width: 34px; height: 34px; border-radius: 50%;
    background: var(--brand-blue);
  }
  .parent-mark .name {
    font-weight: 700; font-size: 27px; color: var(--brand-blue);
    letter-spacing: 0.5px; line-height: 1.1;
  }
  .divider {
    position: absolute; left: 344px; top: 111px;
    width: 1.5px; height: 169px; background: var(--brand-blue);
  }
  .contact {
    position: absolute; left: 373px; top: 106px;
    color: var(--ink); font-size: 16.5px; line-height: 1.25;
  }
  .contact .person {
    font-weight: 700; font-size: 23px; color: var(--brand-blue);
    letter-spacing: 0.6px; line-height: 1.1;
  }
  .contact .title { margin-bottom: 9px; }
  .contact .address { margin-bottom: 9px; }
  .contact .line { margin-bottom: 5px; }
  .brand {
    position: absolute; color: var(--white);
    font-weight: 700; text-transform: uppercase; white-space: nowrap;
  }
  .brand-shoreline { left: 62px; top: 140px; font-size: 27px; letter-spacing: 1px; }
  .brand-spotless {
    left: 44px; top: 222px; font-size: 27px; letter-spacing: 2px;
    display: flex; align-items: center; gap: 12px;
  }
  .brand-spotless .dot {
    width: 44px; height: 44px; border-radius: 50%;
    border: 4px solid var(--light-blue);
  }
  .brand-spotless .label { color: var(--light-blue); }
  .brand-cloudburst {
    left: 430px; top: 160px; width: 230px; text-align: center;
    font-size: 30px; line-height: 1.15; letter-spacing: 1px;
  }
  .brand-cloudburst .square {
    display: block; width: 70px; height: 70px; margin: 0 auto 18px;
    background: var(--white);
  }
</style>
</head>
<body>
  <section class="card card-front" aria-label="Business card front">
    <div class="parent-mark">
      <span class="dot"></span>
      <span class="name">CLEAR HARBOR</span>
    </div>
    <div class="divider"></div>
    <div class="contact">
      <p class="person">DANIEL WHITAKER</p>
      <p class="title">CEO/Founder</p>
      <p class="address">4820 Marina Way Ste 210<br>Harborview 7742</p>
      <p class="line">(555) 284 7310</p>
      <p class="line">info@clearharborcarwash.com</p>
      <p class="line">www.clearharborcarwash.com</p>
    </div>
  </section>

  <section class="card card-back" aria-label="Business card back">
    <p class="brand brand-shoreline">Shoreline Shine</p>
    <p class="brand brand-spotless"><span class="dot"></span><span class="label">Spotless Crew</span></p>
    <p class="brand brand-cloudburst" style="top:70px"><span class="square"></span>Cloudburst<br>Car Wash</p>
  </section>
</body>
</html>
```